Personal Trainer Business Card

I need a business card using a logo I already have.
The logo is in uploaded files.
Card is to give to prospective clients that interested in health and beauty or already exercise. Would like logo on front or other abstract images and details on back.
Like modern design that also unique and eye catching rather than just generic fitness gym/fitness theme.

Target Market(s)

Main clients are trendy women aged 25-60.

Industry/Entity Type

Fitness

Contact Information for Business Card

Email: marc@marcbrevittfitness.com

web: www.marcbrevittfitness.com

mobile: 0432 759208

facebook: www.facebook.com/marcbrevittfitness

Location is: Palm Harbour

Font styles to use
Sans Serif

Colors
000000
1b1b1b
333333

Requirements
Must have
• Logo on front
• black background of sorts on front (fine if mixed with dark grey or abstract)
• White background on back.
Nice to have
• I would like the front side with the logo appearing on it with black background. Fine with alternative ideas and layout.
• Would like the front to be modern, professional and cool/interesting.
• Fine with abstract or modern design.
• Reverse of the card some white background with details on it
• (I like simple fonts).
• CAn use same font colour as in logo in places or what whatever
Should not have
• Avoiding use of cheap pics such as weights

```html
<!DOCTYPE html>
<html lang="en">
<head>
<meta charset="utf-8">
<title>Marc Brevitt Fitness — Business Card</title>
<link href="https://fonts.googleapis.com/css2?family=Barlow+Condensed:wght@200;300;500&display=swap" rel="stylesheet">
<style>
  :root {
    --page: #ffffff;
    --ink-black: #000000;
    --ink-dark: #1b1b1b;
    --ink-mid: #333333;
    --gold: #c2a266;
    --text-grey: #5a5a5a;
    --label-grey: #6b6b6b;
  }
  * { margin: 0; padding: 0; box-sizing: border-box; }
  html, body {
    width: 1200px; height: 1200px; overflow: hidden;
    background: var(--page);
    font-family: "Barlow Condensed", "Arial Narrow", sans-serif;
  }
  .canvas { position: relative; width: 1200px; height: 1200px; }

  .side-label {
    position: absolute;
    left: 88px;
    transform: translate(-50%, -50%) rotate(-90deg);
    font-weight: 200;
    font-size: 54px;
    letter-spacing: 2px;
    color: var(--label-grey);
    white-space: nowrap;
  }
  .side-label--front { top: 253px; }
  .side-label--back { top: 895px; }

  .card {
    position: absolute;
    width: 875px; height: 524px;
    box-shadow: 0 8px 24px rgba(0,0,0,0.12);
  }
  .card--front {
    left: 162px; top: 35px;
    background: radial-gradient(ellipse at 50% 45%, var(--ink-mid) 0%, var(--ink-dark) 55%, #121111 100%);
  }
  .card--back {
    left: 160px; top: 634px;
    background: radial-gradient(ellipse at 50% 50%, #ffffff 40%, #f6f6f6 100%);
    border: 1px solid #e4e4e4;
  }

  .brand {
    position: absolute;
    transform: translate(-50%, -50%);
    text-align: center;
    color: var(--gold);
    font-weight: 500;
    text-transform: uppercase;
    line-height: 1;
    white-space: nowrap;
  }
  .brand__name { display: block; }
  .brand__line { display: block; }
  .brand--front { left: 436px; top: 262px; font-size: 78px; letter-spacing: 3px; }
  .brand--front .brand__line { font-size: 40px; letter-spacing: 14px; margin-top: 8px; }
  .brand--back { left: 230px; top: 262px; font-size: 42px; letter-spacing: 2px; }
  .brand--back .brand__line { font-size: 22px; letter-spacing: 8px; margin-top: 5px; }

  .divider {
    position: absolute;
    left: 428px; top: 142px;
    width: 8px; height: 266px;
    background: linear-gradient(to right, rgba(0,0,0,0.08), rgba(0,0,0,0));
    -webkit-mask: linear-gradient(to bottom, transparent, #000 25%, #000 75%, transparent);
            mask: linear-gradient(to bottom, transparent, #000 25%, #000 75%, transparent);
  }

  .contact-list { list-style: none; }
  .contact {
    position: absolute;
    left: 472px;
    display: flex; align-items: center; gap: 12px;
    transform: translateY(-50%);
    font-weight: 300;
    font-size: 22px;
    letter-spacing: 0.3px;
    color: var(--text-grey);
  }
  .contact svg { width: 26px; height: 26px; flex: none; fill: var(--gold); }
  .contact--email { top: 156px; }
  .contact--phone { top: 225px; }
  .contact--location { top: 306px; }
  .contact--social { top: 379px; }
</style>
</head>
<body>
<main class="canvas">
  <div class="side-label side-label--front">FRONT</div>
  <div class="side-label side-label--back">BACK</div>

  <section class="card card--front" aria-label="Card front">
    <div class="brand brand--front">
      <span class="brand__name">Marc Brevitt</span>
      <span class="brand__line">Fitness</span>
    </div>
  </section>

  <section class="card card--back" aria-label="Card back">
    <div class="brand brand--back">
      <span class="brand__name">Marc Brevitt</span>
      <span class="brand__line">Fitness</span>
    </div>
    <div class="divider"></div>
    <ul class="contact-list">
      <li class="contact contact--email">
        <svg viewBox="0 0 24 24" aria-hidden="true"><path d="M2 5h20v14H2z"/><path d="M3 6.5l9 7 9-7" fill="none" stroke="#fff" stroke-width="1.6"/><path d="M3 18l7-6 M21 18l-7-6" stroke="#fff" stroke-width="1.2"/></svg>
        <span>marc@marcbrevittfitness.com</span>
      </li>
      <li class="contact contact--phone">
        <svg viewBox="0 0 24 24" aria-hidden="true"><path d="M6.6 10.8a15 15 0 0 0 6.6 6.6l2.2-2.2a1 1 0 0 1 1-.25 11.4 11.4 0 0 0 3.6.6 1 1 0 0 1 1 1V20a1 1 0 0 1-1 1A17 17 0 0 1 3 4a1 1 0 0 1 1-1h3.5a1 1 0 0 1 1 1c0 1.25.2 2.45.6 3.6a1 1 0 0 1-.25 1z"/></svg>
        <span>+ 0432 759208</span>
      </li>
      <li class="contact contact--location">
        <svg viewBox="0 0 24 24" aria-hidden="true"><path d="M12 3L1.5 12h3v9h6v-6h3v6h6v-9h3z"/></svg>
        <span>Palm Harbour</span>
      </li>
      <li class="contact contact--social">
        <svg viewBox="0 0 24 24" aria-hidden="true"><circle cx="12" cy="12" r="11"/></svg>
        <span>/marcbrevittfitness</span>
      </li>
    </ul>
  </section>
</main>
</body>
</html>
```